Sleep Consulting Business

Hello I need a business card design with similar colors to my logo that was created. I help mom/parents whose little ones are having sleep issues. Are you able to recreate the picture with the girl sleeping onto a business card using a picture that I provide. That would be one side with my logo on top and on the other side would the following:
My name (in bigger letters than the rest. maybe written in script
title
email
website
phone
instagram
I have included color Inspo
Full Name, number, email, website, ig page

```html
<!DOCTYPE html>
<html lang="en">
<head>
<meta charset="utf-8">
<title>Snug Till Dawn – Business Card</title>
<link rel="stylesheet" href="https://fonts.googleapis.com/css2?family=Lato:wght@400;700&family=Pinyon+Script&display=swap">
<style>
  :root {
    --backdrop: #1f1f1f;
    --card-dark: #444444;
    --card-light: #ffffff;
    --rose: #d49a80;
    --taupe: #9b8f88;
    --ink: #4a4a4a;
  }
  * { box-sizing: border-box; margin: 0; padding: 0; }
  html, body {
    width: 1200px;
    height: 900px;
    overflow: hidden;
    background: var(--backdrop);
  }
  .canvas {
    width: 1200px;
    height: 900px;
    display: flex;
    flex-direction: column;
    align-items: center;
    justify-content: center;
    gap: 48px;
  }
  .card {
    width: 600px;
    height: 343px;
    border-radius: 22px;
    border-bottom: 5px solid var(--rose);
    border-right: 3px solid var(--rose);
    position: relative;
    display: flex;
    flex-direction: column;
    align-items: center;
    justify-content: center;
    font-family: "Lato", sans-serif;
  }
  .card--front { background: var(--card-dark); }
  .card--back { background: var(--card-light); }

  .brand {
    display: flex;
    align-items: center;
    gap: 14px;
    color: var(--rose);
    font-weight: 700;
  }
  .brand__dot {
    border-radius: 50%;
    background: var(--taupe);
  }
  .card--front .brand { font-size: 46px; letter-spacing: 2px; }
  .card--front .brand__dot { width: 40px; height: 40px; }
  .card--back .brand { font-size: 20px; letter-spacing: 1px; margin-bottom: 6px; }
  .card--back .brand__dot { width: 22px; height: 22px; }

  .holder__name {
    font-family: "Pinyon Script", cursive;
    font-size: 64px;
    color: var(--taupe);
    line-height: 1.1;
  }
  .holder__title {
    display: flex;
    align-items: center;
    gap: 10px;
    color: var(--rose);
    font-size: 17px;
    margin-bottom: 12px;
  }
  .holder__title::before,
  .holder__title::after {
    content: "";
    width: 70px;
    height: 1.5px;
    background: var(--taupe);
  }
  .contact {
    list-style: none;
    text-align: center;
    color: var(--ink);
    font-size: 15px;
    line-height: 1.4;
  }
  .contact__phone { font-weight: 700; font-size: 16px; }
  .contact__social { color: var(--rose); margin-top: 8px; font-size: 14px; }
</style>
</head>
<body>
<main class="canvas">
  <section class="card card--front">
    <div class="brand"><span class="brand__dot"></span>Snug Till Dawn</div>
  </section>

  <section class="card card--back">
    <div class="brand"><span class="brand__dot"></span>Snug Till Dawn</div>
    <h1 class="holder__name">Daniel Hart</h1>
    <p class="holder__title">Founder &amp; CEO</p>
    <ul class="contact">
      <li class="contact__phone">(555) 014-2837</li>
      <li>hello@snugtilldawn.com</li>
      <li>snugtilldawn.com</li>
      <li class="contact__social">@snugtilldawn</li>
    </ul>
  </section>
</main>
</body>
</html>
```